Calder Pizza - Takeout Menu Design

We are looking for a takeout menu design.
We are looking for a( 5" x 8.5" DOUBLE SIDED) flyer with our available pizza flavors
Must be easy to ready and not "busy"

Must include our logo (attached)
website: www.calderpizza.ca
address:
Fenwick Ridge Plaza
417, 318 9 Avenue SW
and the following details:
Visit our website for our complete appetizer, pasta, salad and catering menu.

Winner of this contest will also be offered to create a few print designs via printhive.

Please do not hesitate to ask any questions.

Target Market(s)

Business / Office clientele

Industry/Entity Type

Pizza place / specializing in corporate orders

Requirements
Must have
• Easy to read
Should not have
• Can not be busy or cluttered

```html
<!DOCTYPE html>
<html lang="en">
<head>
<meta charset="utf-8">
<title>Calder Pizza – Take-Out Menu</title>
<link rel="stylesheet" href="https://fonts.googleapis.com/css2?family=Poppins:ital,wght@0,300;0,400;0,500;0,600;0,700;1,400&display=swap">
<style>
:root{
  --backdrop:#3a0000;
  --board:#161616;
  --board-light:#262626;
  --red:#e3212b;
  --yellow:#f6e21a;
  --price:#f2d22a;
  --white:#ffffff;
  --strip:#f4f4f4;
}
*{margin:0;padding:0;box-sizing:border-box}
html,body{width:1200px;height:1041px;overflow:hidden;background:var(--backdrop)}
body{position:relative;font-family:'Poppins',sans-serif;color:var(--white)}

.flyer{position:absolute;display:flex;height:660px}
.flyer--front{left:153px;top:104px}
.flyer--back{left:659px;top:277px;height:659px}

.board{position:relative;width:275px;height:100%;overflow:hidden;
  background:repeating-linear-gradient(90deg,rgba(255,255,255,.035) 0 1px,transparent 1px 4px),
  linear-gradient(180deg,var(--board-light),var(--board) 40%,#111);}
.divider{width:9px;height:100%;background:var(--strip)}
.side-photo{width:104px;height:100%;
  background:linear-gradient(180deg,#b57a45 0%,#4a4a3c 18%,#43482f 35%,#9c4a2c 55%,#c9c6bf 72%,#3f4630 84%,#c08a55 100%);}

.brand{position:absolute;left:0;right:0;text-align:center;font-weight:300;font-size:32px;letter-spacing:.5px;line-height:1;color:var(--white);z-index:2}
.flyer--front .brand{top:21px}
.flyer--back .brand{top:19px}

.section-title{position:absolute;left:0;right:0;text-align:center;font-weight:700;font-size:15px;line-height:1;z-index:2}
.section-title--classic{color:var(--yellow);top:73px}
.section-title--speciality{color:var(--white)}

.size-head{position:absolute;color:var(--red);font-size:9px;font-weight:300;font-style:italic;z-index:2}

/* classic list */
.classic{position:absolute;left:23px;top:109px;width:229px;z-index:2}
.classic li{list-style:none;display:flex;align-items:baseline;height:20.7px;font-size:8.6px}
.classic .name{color:var(--red);font-weight:500;white-space:nowrap}
.classic .leader{flex:1;border-bottom:1px dotted var(--red);margin:0 2px;transform:translateY(-2px)}
.classic .p8,.classic .p13{color:var(--price);font-weight:600;text-align:right}
.classic .p8{width:44px}
.classic .p13{width:36px}

.promise{position:absolute;left:0;right:0;top:265px;height:76px;
  background:linear-gradient(90deg,rgba(200,190,20,.25),rgba(170,160,20,.35),rgba(200,190,20,.2));}
.promise p{position:absolute;left:0;right:0;top:17px;text-align:center;font-weight:300;font-size:11px;line-height:15.6px;text-transform:uppercase;letter-spacing:.1px}

/* speciality lists */
.specials{position:absolute;z-index:2}
.item{display:grid;grid-template-columns:1fr 36px 34px;font-size:7.6px;line-height:9.75px}
.item .name{grid-column:1/-1;color:var(--red);font-weight:500;font-size:8.3px}
.item .desc{font-style:italic;font-weight:400;white-space:nowrap}
.item .p8,.item .p13{color:var(--price);font-weight:600;text-align:right;align-self:start;font-size:8.2px}
.item.gap-after{margin-bottom:9.75px}

.flyer--front .specials{left:14px;top:377px;width:250px}
.flyer--back .specials{left:9px;top:90px;width:258px}
.flyer--back .item{line-height:9.88px}

.gst{font-size:6px;font-style:italic;font-weight:400;color:var(--white);z-index:2}
.gst--vertical{position:absolute;left:14px;top:654px;transform-origin:left top;transform:rotate(-90deg);white-space:nowrap}
.gst--inline{position:absolute;left:9px;top:645px}

.visit{position:absolute;left:26px;top:610px;z-index:2;font-size:6px;line-height:8.5px;font-weight:400;color:var(--white)}
.visit .web{color:var(--price);font-weight:600}

.slice{position:absolute;z-index:1;background:radial-gradient(ellipse at 55% 60%,#f06a2a 0%,#d8321c 45%,rgba(120,20,10,.6) 75%,transparent 100%)}
.slice--front{left:100px;top:528px;width:175px;height:132px}
.slice--back{left:100px;top:628px;width:120px;height:31px}
</style>
</head>
<body>

<section class="flyer flyer--front">
  <div class="board">
    <h1 class="brand">CALDER PIZZA</h1>
    <h2 class="section-title section-title--classic">Classic Take-Out Pizza</h2>
    <span class="size-head" style="left:205px;top:98px">8″</span>
    <span class="size-head" style="left:237px;top:98px">13″</span>
    <ul class="classic">
      <li><span class="name">Pepperoni &amp; Mushroom</span><span class="leader"></span><span class="p8">$12.99</span><span class="p13">$30.95</span></li>
      <li><span class="name">Pepperoni</span><span class="leader"></span><span class="p8">$11.99</span><span class="p13">$29.95</span></li>
      <li><span class="name">Hawaiian</span><span class="leader"></span><span class="p8">$12.99</span><span class="p13">$30.95</span></li>
      <li><span class="name">Beef &amp; Mushroom</span><span class="leader"></span><span class="p8">$13.49</span><span class="p13">$32.95</span></li>
      <li><span class="name">Pepperoni &amp; Ham</span><span class="leader"></span><span class="p8">$12.99</span><span class="p13">$30.95</span></li>
      <li><span class="name">Ham &amp; Mushroom</span><span class="leader"></span><span class="p8">$12.99</span><span class="p13">$30.95</span></li>
      <li><span class="name">Beef &amp; Onion</span><span class="leader"></span><span class="p8">$13.49</span><span class="p13">$32.95</span></li>
      <li><span class="name">Cheese</span><span class="leader"></span><span class="p8">$11.99</span><span class="p13">$29.95</span></li>
    </ul>
    <div class="promise"><p>All of our pizzas are prepared fresh<br>everyday using only the finest<br>mozzarella blend and ingredients.</p></div>
    <h2 class="section-title section-title--speciality" style="top:343px">Speciality Take-Out Pizza</h2>
    <span class="size-head" style="left:217px;top:365px">8″</span>
    <span class="size-head" style="left:246px;top:365px">13″</span>
    <div class="specials">
      <div class="item"><p class="name">All Meat</p><p class="desc">Pepperoni, Beef &amp; Smoked Ham &amp; Bacon</p><p class="p8">$14.99</p><p class="p13">$35.95</p></div>
      <div class="item"><p class="name">Double Pepperoni</p><p class="desc">Loads of Pepperoni</p><p class="p8">$13.49</p><p class="p13">$32.95</p></div>
      <div class="item"><p class="name">Hot Honey Pepperoni</p><p class="desc">Double Pepperoni and drizzled with Hot Honey</p><p class="p8">$14.49</p><p class="p13">$34.95</p></div>
      <div class="item"><p class="name">Hawaiian Heat</p><p class="desc">Smoked Ham, Pineapple and Banana Peppers</p><p class="p8">$13.49</p><p class="p13">$32.95</p></div>
      <div class="item"><p class="name">Four Cheese</p><p class="desc">Mozzarella, Feta, Romano and Cheddar Cheese</p><p class="p8">$13.49</p><p class="p13">$32.95</p></div>
      <div class="item"><p class="name">Montreal</p><p class="desc">Pepperoni &amp; Double Smoked Bacon</p><p class="p8">$13.49</p><p class="p13">$32.95</p></div>
      <div class="item"><p class="name">Montreal Heat</p><p class="desc">Pepperoni, Double Smoked Bacon<br>&amp; Banana Peppers</p><p class="p8">$13.99</p><p class="p13">$33.95</p></div>
    </div>
    <address class="visit"><span class="web">www.calderpizza.ca</span><br>Fenwick Ridge Plaza<br>417, 318 9 Avenue SW</address>
    <p class="gst gst--vertical">*All prices are exclusive of GST.</p>
    <div class="slice slice--front" role="img" aria-label="Photo of stacked pizza slices"></div>
  </div>
  <div class="divider"></div>
  <div class="side-photo" role="img" aria-label="Photo of pizza slices on plates over a green cloth"></div>
</section>

<section class="flyer flyer--back">
  <div class="board">
    <h1 class="brand">CALDER PIZZA</h1>
    <h2 class="section-title section-title--speciality" style="top:66px">Speciality Take-Out Pizza</h2>
    <span class="size-head" style="left:222px;top:89px">8″</span>
    <span class="size-head" style="left:252px;top:89px">13″</span>
    <div class="specials">
      <div class="item"><p class="name">Supreme</p><p class="desc">Pepperoni, Mushrooms &amp; Green Peppers</p><p class="p8">$13.49</p><p class="p13">$32.95</p></div>
      <div class="item"><p class="name">Canadian</p><p class="desc">Pepperoni, Mushrooms &amp; Ham</p><p class="p8">$13.49</p><p class="p13">$32.95</p></div>
      <div class="item"><p class="name">BBQ Chicken</p><p class="desc">Chicken Breast, Hickory BBQ Sauce &amp; Red<br>Onions.</p><p class="p8">$13.99</p><p class="p13">$33.95</p></div>
      <div class="item"><p class="name">BBQ Chicken Plus</p><p class="desc">Chicken Breast, Hickory BBQ Sauce, Red<br>Onions &amp; Cilantro</p><p class="p8">$14.79</p><p class="p13">$34.95</p></div>
      <div class="item gap-after"><p class="name">Spicy BBQ Chicken</p><p class="desc">Chicken Breast, Hickory BBQ Sauce</p><p class="p8">$14.49</p><p class="p13">$35.95</p></div>
      <div class="item"><p class="name">Sweet Chili Chicken</p><p class="desc">Chicken Breast, Pineapple, Red Onions &amp;<br>Sweet Chili Sauce</p><p class="p8">$14.49</p><p class="p13">$35.95</p></div>
      <div class="item"><p class="name">Chicken Club</p><p class="desc">Chicken Breast, Double Smoked Bacon<br>Red Onions and Tomatoes</p><p class="p8">$14.79</p><p class="p13">$35.95</p></div>
      <div class="item"><p class="name">Athenean</p><p class="desc">Chicken Breast, Spinach, Feta Cheese and<br>Tomato</p><p class="p8">$14.49</p><p class="p13">$34.95</p></div>
      <div class="item"><p class="name">Greek Supreme</p><p class="desc">Chicken Breast, Feta Cheese, Tomato<br>Green Pepper, Red Onions &amp; Black Olives</p><p class="p8">$14.99</p><p class="p13">$35.95</p></div>
      <div class="item"><p class="name">Mediterranean Chicken</p><p class="desc">Seasoned Chicken Breast, Tomatoes,<br>Red Onions and Feta Cheese</p><p class="p8">$14.79</p><p class="p13">$35.95</p></div>
      <div class="item"><p class="name">Original Spinach</p><p class="desc">Spinach &amp; Feta Cheese</p><p class="p8">$13.49</p><p class="p13">$32.95</p></div>
      <div class="item"><p class="name">Zeus</p><p class="desc">Spinach, Feta Cheese and Tomatoes</p><p class="p8">$13.95</p><p class="p13">$33.95</p></div>
      <div class="item"><p class="name">Greek</p><p class="desc">Feta Cheese, Tomato, Green Peppers<br>Red Onions and Black Olives</p><p class="p8">$13.99</p><p class="p13">$33.95</p></div>
      <div class="item"><p class="name">Vegetarian</p><p class="desc">Mushrooms, Tomatoes, Green Peppers and<br>Black Olives</p><p class="p8">$13.49</p><p class="p13">$32.95</p></div>
      <div class="item"><p class="name">Veggie Delight</p><p class="desc">Mushrooms, Tomatoes, Green Peppers, Black<br>Olives &amp; Onion</p><p class="p8">$13.95</p><p class="p13">$33.95</p></div>
      <div class="item"><p class="name">Deluxe</p><p class="desc">Pepperoni, Mushrooms, Ham, Tomatoes<br>Green Peppers and Red Onions</p><p class="p8">$14.49</p><p class="p13">$34.95</p></div>
      <div class="item"><p class="name">Calder Special</p><p class="desc">Pepperoni, Mushrooms, Ham, Green Peppers<br>and Black Olives</p><p class="p8">$14.49</p><p class="p13">$34.95</p></div>
      <div class="item"><p class="name">Dill Pickle</p><p class="desc">Crispy Dill Pickles, Fresh Dill with our cream<br>based garlic sauce.</p><p class="p8">$13.49</p><p class="p13">$32.95</p><p class="desc">Served with without bacon.</p><p class="p8">$14.49</p><p class="p13">$35.95</p></div>
      <div class="item"><p class="name">BBQ Pulled Pork</p><p class="desc">Pulled Pork, Red Onions<br>Red Peppers and Cilantro.</p><p class="p8">$14.49</p><p class="p13">$35.95</p></div>
    </div>
    <p class="gst gst--inline">*All prices are exclusive of GST.</p>
    <div class="slice slice--back" role="img" aria-label="Photo of a pizza slice"></div>
  </div>
  <div class="divider"></div>
  <div class="side-photo" role="img" aria-label="Photo of pizza slices on plates over a green cloth"></div>
</section>

</body>
</html>
```